Hollow Birch Vintners Reserve Cabernet Sauvignon Wine Labels front and back

I need a front and back wine label. For a new RESERVE Cabernet Sauvignon wine. I am attaching the details and some ideas and possible images to use. But creativity is encouraged. This wine will be seen on wine shop and grocery store shelves so it needs to pop while appearing elegant and to be about $50/bottle of wine. The front and back labels should go together nicely. I would like some foil on the front, but not the back. We are trying to show the natural beauty of our vineyards and the elegance of our wines. We would like to invoke a feel of sustainability, proudly family owned and operated.

Target Market(s)

21-50 year olds, red wine drinkers, higher priced wine drinkers

Industry/Entity Type

Wine

Font styles to use
Serif
Script

Colors

Designer to choose only greyscale colors for use in the design.

Requirements
Must have
• Front Label with specified details and Back label with specified details. Foil banner on the front label that says " Family stewards of the land for 5 generations"the front label that says
Nice to have
• vineyard or winery background, have include a sample or example, some gold or bronze or silver accents

```html
<!DOCTYPE html>
<html lang="en">
<head>
<meta charset="utf-8">
<title>Hollow Birch Vintners Reserve – Front and Back Labels</title>
<link rel="stylesheet" href="https://fonts.googleapis.com/css2?family=Cinzel:wght@500;600;700&family=Crimson+Text:wght@400&family=Pinyon+Script&family=Allura&display=swap">
<style>
  :root{
    --canvas:#ffffff;
    --cream:#fdf2de;
    --maroon:#6e1a1a;
    --copper:#c8803e;
    --ink:#5a1414;
    --white:#ffffff;
  }
  *{box-sizing:border-box;margin:0;padding:0}
  html,body{width:1200px;height:1200px;overflow:hidden;background:var(--canvas)}
  .canvas{position:relative;width:1200px;height:1200px}

  /* Front label */
  .front-label{position:absolute;left:265px;top:352px;width:333px;height:509px;background:var(--cream);border-radius:6px;overflow:hidden;color:var(--maroon)}
  .front-label .rule{position:absolute;left:0;right:0;top:44px;height:5px;border-top:1px solid var(--copper);border-bottom:1px solid var(--copper)}
  .brand-mark{position:absolute;left:0;right:0;top:34px;display:flex;justify-content:center;align-items:center;gap:6px}
  .brand-mark .mark-square{width:24px;height:24px;background:var(--maroon);border:2px solid var(--copper)}
  .brand-mark .mark-name{font-family:"Cinzel",serif;font-weight:600;font-size:9px;letter-spacing:.08em;color:var(--maroon);background:var(--cream);padding:0 5px;line-height:24px}
  .front-title{position:absolute;left:0;right:0;top:100px;text-align:center;font-family:"Cinzel",serif;font-weight:600;font-size:29px;line-height:30px;letter-spacing:.01em}
  .reserve{position:absolute;left:0;right:0;top:190px;text-align:center;font-family:"Pinyon Script",cursive;font-size:50px;line-height:60px;color:var(--copper)}
  .region-arc{position:absolute;left:60px;top:248px;width:213px;height:50px}
  .region-arc text{font-family:"Cinzel",serif;font-weight:600;font-size:13px;letter-spacing:.08em;fill:var(--maroon)}
  .barrels{position:absolute;left:112px;top:282px;width:122px;height:113px;border-radius:40% 40% 10% 10%;background:radial-gradient(ellipse at 50% 45%,#8a2a22 0%,#6e1a1a 60%,rgba(110,26,26,.2) 100%)}
  .varietal{position:absolute;left:0;right:0;top:418px;text-align:center;font-family:"Cinzel",serif;font-weight:700;font-size:10.5px;letter-spacing:.14em}
  .vintage{position:absolute;left:0;right:0;top:432px;text-align:center;font-family:"Crimson Text",serif;font-size:12px;letter-spacing:.08em}
  .foil-banner{position:absolute;left:0;right:0;bottom:0;height:36px;background:var(--maroon);display:flex;align-items:center;justify-content:center;font-family:"Crimson Text",serif;font-size:10px;letter-spacing:.12em;color:var(--cream);text-transform:uppercase}

  /* Back label */
  .back-label{position:absolute;left:631px;top:428px;width:305px;height:357px;background:var(--cream);border-radius:8px;color:var(--ink)}
  .back-title{position:absolute;left:0;right:0;top:30px;text-align:center;font-family:"Cinzel",serif;font-weight:600;font-size:16px;letter-spacing:.01em;color:var(--maroon)}
  .story{position:absolute;left:30px;right:30px;top:62px;text-align:center;font-family:"Crimson Text",serif;font-size:9.6px;line-height:13px}
  .signature{position:absolute;left:0;right:0;top:134px;text-align:center;font-family:"Allura",cursive;font-size:32px;color:var(--copper)}
  .sign-off{position:absolute;left:0;right:0;top:173px;text-align:center;font-family:"Crimson Text",serif;font-size:9.6px;line-height:11px}
  .warning{position:absolute;left:11px;width:162px;top:245px;font-family:"Crimson Text",serif;font-size:8.4px;line-height:13px}
  .divider{position:absolute;left:175px;top:231px;height:100px;border-left:1px solid var(--copper)}
  .facts{position:absolute;left:181px;right:12px;top:231px;font-family:"Crimson Text",serif;font-size:8.6px;line-height:11px;text-transform:uppercase}
  .facts .producer{margin-top:3px;font-size:5px;line-height:7px}
  .barcode-space{position:absolute;left:181px;top:286px;width:111px;height:43px;background:var(--white)}
</style>
</head>
<body>
<main class="canvas">

  <section class="front-label" aria-label="Front label">
    <div class="rule"></div>
    <div class="brand-mark">
      <span class="mark-square"></span>
      <span class="mark-name">HOLLOW BIRCH VINTNERS</span>
    </div>
    <h1 class="front-title">HOLLOW BIRCH<br>VINTNERS</h1>
    <div class="reserve">Reserve</div>
    <svg class="region-arc" viewBox="0 0 213 50" aria-label="Horse Heaven Hills">
      <defs><path id="regionPath" d="M8,46 Q106,-2 205,46"/></defs>
      <text><textPath href="#regionPath" startOffset="50%" text-anchor="middle">· Horse Heaven Hills ·</textPath></text>
    </svg>
    <div class="barrels" role="img" aria-label="Engraved illustration of stacked oak wine barrels"></div>
    <div class="varietal">CABERNET SAUVIGNON</div>
    <div class="vintage">2022</div>
    <div class="foil-banner">Family stewards of the land for 5 generations</div>
  </section>

  <section class="back-label" aria-label="Back label">
    <h2 class="back-title">HOLLOW BIRCH VINTNERS</h2>
    <p class="story">"Our vineyards, nestled along the Columbia River in Washington state, flourish in a region celebrated for its long, hot days and cool, crisp nights. This area, rich in natural resources and fertile soils, imparts a unique essence of balance, structure, and elegance to our wines."</p>
    <div class="signature">Maren Holloway</div>
    <p class="sign-off">Cheers<br>Maren Holloway<br>Winemaker</p>
    <p class="warning">GOVERNMENT WARNING:<br>(1) According to the Surgeon General, women should not drink alcoholic beverages during pregnancy because of the risk of birth defects. (2) Consumption of alcoholic beverages impairs your ability to drive a car or operate machinery, and may cause health problems.</p>
    <div class="divider"></div>
    <div class="facts">
      <p>750 ML<br>Contains sulfites<br>15% alc. by vol.</p>
      <p class="producer">Produced and bottled by Ridgeway<br>Wine Estates, LLC, Alder Falls WA, USA</p>
    </div>
    <div class="barcode-space"></div>
  </section>

</main>
</body>
</html>
```